Hair Salon Brochure

We need a brochure for our hair salon located in Middle Tennessee called Delphine Locks of Harbor Bend. Along with standard services, we offer specialized services and accommodations for individuals on the Autism Spectrum, regardless of background or hair type.
At Delphine Locks of Harbor Bend, our mission is to create a warm and inclusive haven for individuals of all backgrounds, including those on the autism spectrum and their families. We are dedicated to providing not only exceptional hairstyling services but also hands-on education and specialized cutting techniques for clients with natural textured hair. Our goal is to empower our clients with the knowledge and tools necessary to maintain a successful hair care routine, ensuring they leave our salon feeling confident.
We believe in fostering a sense of community, where parents of younger clients are encouraged to learn the proper hair care techniques for their children, promoting healthy practices at home. Our commitment extends beyond just hair; we are here to help you embrace your true self and recognize the beauty that resides within.
At Delphine Locks of Harbor Bend, our passion is to deliver the ultimate client experience, where you can be unapologetically yourself and feel completely at ease. From the moment you step through our doors, you are welcomed not only to discuss your hair concerns but also to engage in meaningful conversations about life. Together, we will collaborate on a personalized plan to achieve your hair goals and transform the way you perceive yourself.
Always remember, when you look good, you feel good, and when you feel good, you can achieve great things. We firmly believe that every individual is 'Beautiful Beyond the Spectrum,' and we are here to celebrate that beauty with you."
https://www.delphinelocks.net/
Tagline - "Beautiful Beyond the Spectrum"

```html
<!DOCTYPE html>
<html lang="en">
<head>
<meta charset="utf-8">
<title>Delphine Locks of Harbor Bend — Expert Hair Treatments</title>
<link href="https://fonts.googleapis.com/css2?family=Comfortaa:wght@300;400;700&family=Kaushan+Script&display=swap" rel="stylesheet">
<style>
  :root {
    --page: #3a3a3c;
    --purple: #4a36bd;
    --purple-deep: #5a2fc6;
    --panel: #e9e8ee;
    --orange: #e8730f;
    --orange-deep: #d95f0c;
    --lavender: #b8aef2;
    --white: #ffffff;
    --ink: #3b2aa8;
    --logo-blue: #1f7fc8;
    --photo-dark: #1d2a44;
    --photo-warm: #8a6a4c;
  }
  * { box-sizing: border-box; margin: 0; padding: 0; }
  html, body { width: 1200px; height: 923px; overflow: hidden; background: var(--page); }
  .flyer {
    position: absolute; left: 296px; top: 31px; width: 608px; height: 860px;
    overflow: hidden; background: linear-gradient(160deg, var(--purple), var(--purple-deep));
    font-family: "Comfortaa", sans-serif; color: var(--white);
    box-shadow: 0 10px 30px rgba(0,0,0,.4);
  }
  .flyer-shapes { position: absolute; inset: 0; }
  .photo-circle {
    position: absolute; width: 130px; height: 130px; border-radius: 50%;
    border: 5px solid var(--white);
  }
  .photo-circle--styling { left: -10px; top: 335px; background: linear-gradient(135deg, #c9b3a8, #6e4a3a); }
  .photo-circle--wash { left: 126px; top: 328px; background: linear-gradient(135deg, #f0ece8, #9a8e86); }
  .brand {
    position: absolute; left: 392px; top: 214px; width: 200px;
    display: flex; align-items: center; gap: 8px;
    color: var(--logo-blue); font-weight: 700; font-size: 16px; line-height: 1.25;
  }
  .brand-dot { flex: none; width: 16px; height: 16px; border-radius: 50%; background: var(--logo-blue); }
  .headline { position: absolute; right: 28px; top: 404px; text-align: right; font-family: "Kaushan Script", cursive; font-weight: 400; line-height: 1; }
  .headline-main { display: block; font-size: 56px; color: var(--white); }
  .headline-sub { display: block; font-size: 46px; color: var(--orange); margin-top: 2px; }
  .services { position: absolute; left: 40px; top: 528px; }
  .services-title { font-family: "Kaushan Script", cursive; font-size: 34px; color: var(--orange); font-weight: 400; margin-bottom: 8px; }
  .services-list { list-style: none; }
  .services-list li { font-size: 15px; font-weight: 700; margin-bottom: 8px; display: flex; align-items: center; gap: 12px; white-space: nowrap; }
  .services-list li::before { content: ""; flex: none; width: 8px; height: 8px; border-radius: 50%; background: var(--logo-blue); border: 2px solid var(--lavender); }
  .tagline { position: absolute; right: 28px; top: 548px; text-align: right; color: var(--lavender); font-size: 18px; line-height: 1.55; letter-spacing: 1.5px; font-weight: 700; white-space: nowrap; }
  .stylist-card {
    position: absolute; left: 276px; top: 628px; width: 304px; height: 90px;
    background: var(--white); border-radius: 26px; display: flex; align-items: center; gap: 14px; padding: 7px;
    box-shadow: 0 4px 10px rgba(0,0,0,.25);
  }
  .stylist-photo { flex: none; width: 76px; height: 76px; border-radius: 20px; background: linear-gradient(135deg, #d9cfc6, #3c2a24); }
  .stylist-name { color: var(--ink); font-weight: 700; font-size: 19px; }
  .stylist-role { color: var(--ink); font-size: 12px; font-weight: 700; margin-top: 4px; }
  .contact { position: absolute; left: 40px; top: 732px; }
  .contact-label { font-size: 12px; letter-spacing: 1px; }
  .contact-phone { font-size: 27px; font-weight: 700; letter-spacing: 1px; margin: 4px 0 8px; }
  .contact-line { display: flex; align-items: center; gap: 10px; font-size: 14px; margin-bottom: 6px; font-weight: 300; }
  .contact-icon { flex: none; width: 18px; height: 18px; border-radius: 50%; background: var(--orange); }
  .motto { position: absolute; right: 28px; top: 748px; text-align: right; white-space: nowrap; }
  .motto-light { display: block; font-size: 32px; font-weight: 300; }
  .motto-script { display: block; font-family: "Kaushan Script", cursive; font-size: 34px; margin-top: 2px; }
</style>
</head>
<body>
<main class="flyer">
  <svg class="flyer-shapes" viewBox="0 0 608 860" width="608" height="860" aria-hidden="true">
    <defs>
      <linearGradient id="photoTone" x1="0" y1="0" x2="1" y2="1">
        <stop offset="0" stop-color="var(--photo-warm)"/>
        <stop offset=".35" stop-color="var(--photo-dark)"/>
        <stop offset="1" stop-color="#2c3650"/>
      </linearGradient>
      <linearGradient id="swoosh" x1="0" y1="0" x2="1" y2="1">
        <stop offset="0" stop-color="var(--orange)"/>
        <stop offset="1" stop-color="var(--orange-deep)"/>
      </linearGradient>
    </defs>
    <path d="M0 0 H440 C420 130 380 230 320 285 C280 318 240 330 190 334 H0 Z" fill="url(#photoTone)" role="img" aria-label="Salon window with blinds and glowing sign"/>
    <path d="M230 0 H608 V340 C590 250 560 170 470 110 C400 70 310 30 230 0 Z" fill="#7c46c2"/>
    <path d="M220 0 H608 V250 C585 170 530 100 440 60 C370 30 290 14 220 0 Z" fill="url(#swoosh)"/>
    <path d="M448 88 C525 100 572 150 588 240 L590 332 C520 356 400 362 290 336 C360 278 412 195 448 88 Z" fill="var(--panel)" stroke="#6b4fe0" stroke-width="3"/>
    <path d="M560 240 C578 250 590 270 590 300 V332 C578 320 568 290 560 240 Z" fill="var(--lavender)" opacity=".8"/>
    <path d="M305 338 C400 356 520 352 590 322" fill="none" stroke="#8aa6d8" stroke-width="1" stroke-dasharray="4 4"/>
  </svg>

  <div class="photo-circle photo-circle--styling" role="img" aria-label="Stylist blow-drying a smiling client's hair"></div>
  <div class="photo-circle photo-circle--wash" role="img" aria-label="Client relaxing at the wash basin during a shampoo"></div>

  <div class="brand"><span class="brand-dot"></span><span>Delphine Locks<br>of Harbor Bend</span></div>

  <h1 class="headline"><span class="headline-main">Expert Hair</span><span class="headline-sub">Treatments</span></h1>

  <section class="services">
    <h2 class="services-title">Our Services:</h2>
    <ul class="services-list">
      <li>Haircut and Styling</li>
      <li>Hair Coloring</li>
      <li>Hair Extensions</li>
      <li>Blowouts</li>
      <li>Autism-Friendly Care</li>
    </ul>
  </section>

  <p class="tagline">We are not just a salon,<br>we are an experience!</p>

  <div class="stylist-card">
    <div class="stylist-photo" role="img" aria-label="Portrait of the salon's lead stylist"></div>
    <div>
      <p class="stylist-name">Marisol Bennett</p>
      <p class="stylist-role">Stylist / Curl Specialist</p>
    </div>
  </div>

  <section class="contact">
    <p class="contact-label">CALL US</p>
    <p class="contact-phone">555-014-2871</p>
    <p class="contact-line"><span class="contact-icon"></span>@delphinelocksofhb</p>
    <p class="contact-line"><span class="contact-icon"></span>www.delphinelocks.net</p>
  </section>

  <p class="motto"><span class="motto-light">Beautiful</span><span class="motto-script">Beyond the Spectrum</span></p>
</main>
</body>
</html>
```